Doors for Chiropractic Office

In my chiropractic office I have 6 treatment rooms and 2 massage rooms. The entire office is going through a remodel. The overall color scheme is very earth tones but in order to add some color, the 6 doors to the treatment rooms will all be a separate color (Red, Blue, Yellow, Green etc)
I need to number each room 1,2,3,4,5,6 and the 2 massage rooms. I had the idea of putting a giant number on each door, so I am looking for some graphic ideas for that project.
The rooms are located with 4 on each side of a long hallway with the 2 massage rooms at the end.
The purpose of numbering each door is to direct the patients where to go.
I have uploaded pictures of the hall way. Pardon the dust since we are under construction but hopefully it gives you an idea of the layout. The door colors will change as stated above.

Requirements
Nice to have
• I would like to see someone come up with a design where each number for the doors are created out of vertebrae's.

```html
<!DOCTYPE html>
<html lang="en">
<head>
<meta charset="utf-8">
<title>Door Signs – Treatment and Massage Rooms</title>
<link href="https://fonts.googleapis.com/css2?family=Lato:wght@700;900&display=swap" rel="stylesheet">
<style>
  :root {
    --wall: #808085;
    --plate: #f0f0f0;
    --sky: #2ba9e0;
    --slate: #808085;
    --emblem-soft: #cfe3ee;
    --emblem-deep: #a9d3ea;
  }
  html, body {
    margin: 0;
    padding: 0;
    overflow: hidden;
  }
  .board {
    position: relative;
    width: 1200px;
    height: 725px;
    background: var(--wall);
    overflow: hidden;
    font-family: "Lato", Arial, sans-serif;
  }
  .sign {
    position: absolute;
    background: var(--plate);
    border-radius: 9px;
    box-sizing: border-box;
  }
  .sign--door { width: 178px; height: 255px; }
  .sign--massage { width: 237px; height: 262px; border-radius: 20px; }

  .sign__frame {
    position: absolute;
    inset: 8px;
    border: 5px solid var(--sky);
    border-radius: 13px;
  }
  /* openings in the left and right edges of the frame */
  .sign__frame::before,
  .sign__frame::after {
    content: "";
    position: absolute;
    top: 42%;
    height: 16%;
    width: 9px;
    background: var(--plate);
  }
  .sign__frame::before { left: -7px; }
  .sign__frame::after { right: -7px; }

  .sign__number {
    position: absolute;
    z-index: 2;
    top: 13px;
    left: 0;
    width: 158px;
    text-align: center;
    font-weight: 900;
    font-size: 128px;
    line-height: 1;
    color: var(--sky);
  }
  .sign__mark {
    position: absolute;
    z-index: 1;
    left: 60px;
    top: 112px;
    width: 72px;
    height: 110px;
    border-radius: 36px;
    background: linear-gradient(160deg, var(--emblem-soft), var(--emblem-deep));
  }

  .sign__illustration {
    position: absolute;
    left: 43px;
    top: 36px;
    width: 138px;
    height: 109px;
    border-radius: 14px;
    background: linear-gradient(135deg, var(--emblem-deep), var(--emblem-soft));
  }
  .sign__label {
    position: absolute;
    left: 0;
    right: 0;
    top: 150px;
    text-align: center;
    color: var(--slate);
    font-weight: 700;
    font-size: 30px;
    line-height: 29px;
    letter-spacing: -0.5px;
  }
  .sign__room-number {
    display: block;
    color: var(--sky);
    font-size: 35px;
    line-height: 36px;
    margin-top: 3px;
  }
</style>
</head>
<body>
<main class="board">
  <section class="sign sign--door" style="left:114px; top:55px;">
    <div class="sign__frame"></div>
    <div class="sign__mark" role="img" aria-label="Spine emblem with circle"></div>
    <div class="sign__number">1</div>
  </section>
  <section class="sign sign--door" style="left:379px; top:55px;">
    <div class="sign__frame"></div>
    <div class="sign__mark" role="img" aria-label="Spine emblem with circle"></div>
    <div class="sign__number">2</div>
  </section>
  <section class="sign sign--door" style="left:644px; top:55px;">
    <div class="sign__frame"></div>
    <div class="sign__mark" role="img" aria-label="Spine emblem with circle"></div>
    <div class="sign__number">3</div>
  </section>
  <section class="sign sign--door" style="left:909px; top:55px;">
    <div class="sign__frame"></div>
    <div class="sign__mark" role="img" aria-label="Spine emblem with circle"></div>
    <div class="sign__number">4</div>
  </section>

  <section class="sign sign--door" style="left:72px; top:393px;">
    <div class="sign__frame"></div>
    <div class="sign__mark" role="img" aria-label="Spine emblem with circle"></div>
    <div class="sign__number">5</div>
  </section>
  <section class="sign sign--door" style="left:337px; top:393px;">
    <div class="sign__frame"></div>
    <div class="sign__mark" role="img" aria-label="Spine emblem with circle"></div>
    <div class="sign__number">6</div>
  </section>

  <section class="sign sign--massage" style="left:589px; top:383px;">
    <div class="sign__frame"></div>
    <div class="sign__illustration" role="img" aria-label="Spine emblem beside a line icon of a therapist massaging a client"></div>
    <div class="sign__label">MASSAGE<br>ROOM<span class="sign__room-number">1</span></div>
  </section>
  <section class="sign sign--massage" style="left:892px; top:383px;">
    <div class="sign__frame"></div>
    <div class="sign__illustration" role="img" aria-label="Spine emblem beside a line icon of a therapist massaging a client"></div>
    <div class="sign__label">MASSAGE<br>ROOM<span class="sign__room-number">2</span></div>
  </section>
</main>
</body>
</html>
```